Business Card Design Competition

We need a business card design for our Internet Marketing company. We require both front and back designs and the final card must be 89x53mm in size, plus crop marks to 91x55mm. Colours as per logo, plus perhaps black and/or grey (#828282).
Final text must be editable (if you can supply an editable Fireworks PNG, even better)...
FRONT TEXT:
Full Name
Position
Address Line
Suburb, State, Postcode
Phone: 0000 000 000
Mobile: 0000 000 000
Email: xxx@brimleafpromo.com.au
Web: www.brimleafpromo.com.au
Rear of card should be a fresh design plus our slogan text: "Helping You Stand Out" in large font, then in small text "Brimleaf Holdings Pty Ltd (ABN: 42 563 701 384)".
Target Market(s)
Small/Medium Businesses
Industry/Entity Type
Business
Look and feel
Each slider illustrates characteristics of the customer's brand and the style your logo design should communicate.

```html
<!DOCTYPE html>
<html lang="en">
<head>
<meta charset="utf-8">
<title>Brimleaf Promo – Business Card Front and Back</title>
<link rel="stylesheet" href="https://fonts.googleapis.com/css2?family=Open+Sans:wght@400;700&family=Questrial&display=swap">
<style>
  :root {
    --page-bg: #e4e4e2;
    --card-grey: #3c3c3c;
    --card-dark: #252525;
    --brand-orange: #f7941d;
    --brand-amber: #fbb040;
    --brand-green: #8dc63f;
    --text-light: #ffffff;
    --text-soft: #e6e6e6;
  }
  * { box-sizing: border-box; margin: 0; padding: 0; }
  html, body { width: 1200px; height: 900px; overflow: hidden; }
  body { background: var(--page-bg); font-family: "Open Sans", Arial, sans-serif; }
  .canvas { position: relative; width: 1200px; height: 900px; }

  .card {
    position: absolute;
    top: 288px;
    width: 545px;
    height: 312px;
    border-radius: 14px;
    overflow: hidden;
    background: var(--card-dark);
  }
  .card--front { left: 40px; }
  .card--back { left: 618px; background: var(--card-grey); }

  /* Front: plain split panel with a straight accent rule */
  .panel { position: absolute; top: 0; bottom: 0; left: 0; width: 250px; background: var(--card-grey); }
  .accent-rule { position: absolute; top: 0; bottom: 0; width: 4px; background: var(--brand-orange); }
  .card--front .accent-rule { left: 250px; }

  .brand-mark { position: absolute; border-radius: 50%; background: var(--brand-green); }
  .card--front .brand-mark { left: 75px; top: 58px; width: 100px; height: 100px; }
  .brand-name {
    position: absolute;
    font-family: "Questrial", Arial, sans-serif;
    color: var(--brand-orange);
    font-weight: 400;
    line-height: 1;
  }
  .card--front .brand-name { left: 0; width: 250px; text-align: center; top: 184px; font-size: 30px; }
  .brand-name span { display: block; }
  .brand-name span + span { margin-top: 4px; }

  .contact { position: absolute; left: 290px; top: 64px; color: var(--text-light); }
  .contact__name { font-weight: 700; font-size: 22px; line-height: 1.1; }
  .contact__role { font-size: 14px; color: var(--text-soft); margin-top: 2px; }
  .contact__address { font-size: 11.5px; line-height: 16px; margin-top: 24px; color: var(--text-soft); }
  .contact__list { list-style: none; font-size: 11.5px; color: var(--text-soft); }
  .contact__list--phones { margin-top: 12px; }
  .contact__list--online { margin-top: 14px; }
  .contact__list li { display: flex; align-items: center; height: 17px; }
  .contact__icon { width: 12px; height: 12px; margin-right: 10px; fill: var(--text-light); flex: none; }

  /* Back */
  .card--back .accent-rule { left: 0; right: 0; top: auto; bottom: 0; width: auto; height: 4px; }
  .card--back .brand-mark { left: 158px; top: 74px; width: 80px; height: 80px; }
  .card--back .brand-name { left: 250px; top: 80px; font-size: 30px; }
  .card--back .brand-name span + span { margin-top: 2px; }
  .slogan {
    position: absolute;
    left: 0; width: 545px; top: 174px;
    text-align: center;
    font-family: "Questrial", Arial, sans-serif;
    font-size: 24px;
    letter-spacing: 2.5px;
    color: var(--text-light);
  }
  .legal {
    position: absolute;
    left: 0; width: 545px; top: 276px;
    text-align: center;
    font-family: Arial, Helvetica, sans-serif;
    font-size: 11.5px;
    color: var(--text-light);
  }
</style>
</head>
<body>
<main class="canvas">

  <section class="card card--front" aria-label="Business card front">
    <div class="panel" aria-hidden="true"></div>
    <div class="accent-rule" aria-hidden="true"></div>

    <div class="brand-mark" aria-hidden="true"></div>
    <p class="brand-name"><span>Brimleaf</span><span>Promo</span></p>

    <div class="contact">
      <p class="contact__name">Nora Castell</p>
      <p class="contact__role">Company Director</p>
      <p class="contact__address">17 Harrow Lane, Kelvinside<br>Westmoor WM4 2QF 5678</p>
      <ul class="contact__list contact__list--phones">
        <li>
          <svg class="contact__icon" viewBox="0 0 12 12" aria-label="Mobile"><rect x="3" y="0.5" width="6" height="11" rx="1.2"/><rect x="4" y="2" width="4" height="6" fill="var(--card-dark)"/></svg>
          061-555-0148
        </li>
        <li>
          <svg class="contact__icon" viewBox="0 0 12 12" aria-label="Phone"><path d="M1 3.5 Q6 0.5 11 3.5 L10 5.5 L8 4.6 L8 3.6 Q6 3 4 3.6 L4 4.6 L2 5.5 Z"/><rect x="2.5" y="6" width="7" height="5" rx="1"/></svg>
          061-555-0192
        </li>
      </ul>
      <ul class="contact__list contact__list--online">
        <li>
          <svg class="contact__icon" viewBox="0 0 12 12" aria-label="Email"><rect x="0.5" y="2" width="11" height="8" fill="none" stroke="var(--text-light)" stroke-width="1.2"/><path d="M0.5 2 L6 6.5 L11.5 2" fill="none" stroke="var(--text-light)" stroke-width="1.2"/></svg>
          nora@brimleafpromo.com.au
        </li>
        <li>
          <svg class="contact__icon" viewBox="0 0 12 12" aria-label="Website"><circle cx="6" cy="6" r="5.2" fill="none" stroke="var(--text-light)" stroke-width="1.1"/><ellipse cx="6" cy="6" rx="2.2" ry="5.2" fill="none" stroke="var(--text-light)" stroke-width="1"/><path d="M0.8 6 H11.2" stroke="var(--text-light)" stroke-width="1"/></svg>
          brimleafpromo.com.au
        </li>
      </ul>
    </div>
  </section>

  <section class="card card--back" aria-label="Business card back">
    <div class="accent-rule" aria-hidden="true"></div>
    <div class="brand-mark" aria-hidden="true"></div>
    <p class="brand-name"><span>Brimleaf</span><span>Promo</span></p>
    <p class="slogan">Helping You Stand Out</p>
    <p class="legal">Brimleaf Holdings Pty Ltd (ABN: 42 563 701 384)</p>
  </section>

</main>
</body>
</html>
```